Managed Service Provider need new business cards

We are a small Maanged Service Provider of IT Services and need a new fresh design for our business cards. We want something impossible, fun and professional :)
Our services has a large range, but we are always fun and make sure our customers both get their issue sorted and also feel like they are "catching up with an old friend".
All our cards in the past has always been all black, with red and we need something fresher.
The back of card, we would like just a small list of what we do i think, but if someone has a better idea, please do something cool with the back of the card:
Managed IT Services
Productivity Solutions
Data Backup and Recovery
IT System Maintenance
Managed IT Security
More details can be found on our website qvtechworks.com.au
Industry/Entity Type
It Company
Contact Information for Business Card
Name: Simon Trelawny
Title: Director
Phone: 03 6158 4932
Mobile: 0417 582 139
Email: simon@qvtechworks.com.au
Web: www.qvtechworks.com.au
Look and feel
Each slider illustrates characteristics of the customer's brand and the style your logo design should communicate.

```html
<!DOCTYPE html>
<html lang="en">
<head>
<meta charset="utf-8">
<title>QV TechWorks – Business Cards</title>
<link href="https://fonts.googleapis.com/css2?family=Montserrat:wght@400;500;600;800&display=swap" rel="stylesheet">
<style>
  :root {
    --backdrop: #2a2a2a;
    --card-black: #060606;
    --card-sheen: #1a1a1a;
    --brand-red: #e8202a;
    --white: #ffffff;
    --soft-white: #e9e9e9;
  }
  * { margin: 0; padding: 0; box-sizing: border-box; }
  html, body { width: 1200px; height: 930px; overflow: hidden; }
  body {
    background: var(--backdrop);
    font-family: "Montserrat", sans-serif;
    position: relative;
  }
  .card {
    position: absolute;
    width: 560px;
    height: 320px;
    border-radius: 18px;
    background: linear-gradient(115deg, var(--card-black) 0%, var(--card-sheen) 45%, var(--card-black) 70%);
    box-shadow: 0 18px 40px rgba(0,0,0,.55);
    overflow: hidden;
  }
  .card--back { left: 80px; top: 90px; }
  .card--front { left: 560px; top: 500px; }

  .brand {
    position: absolute;
    display: flex;
    align-items: center;
    gap: 12px;
  }
  .brand__name {
    color: var(--brand-red);
    font-weight: 800;
    letter-spacing: 1px;
    white-space: nowrap;
  }
  .brand__dot {
    border-radius: 50%;
    background: var(--white);
  }
  .card--back .brand { left: 0; right: 0; top: 100px; justify-content: center; }
  .card--back .brand__name { font-size: 44px; }
  .card--back .brand__dot { width: 34px; height: 34px; }

  .services {
    position: absolute;
    left: 0; right: 0; bottom: 44px;
    text-align: center;
    color: var(--soft-white);
    font-size: 13px;
    font-weight: 600;
    line-height: 22px;
  }
  .services .sep { color: var(--brand-red); margin: 0 6px; }

  .card--front .brand { left: 34px; top: 92px; }
  .card--front .brand__name { font-size: 26px; }
  .card--front .brand__dot { width: 22px; height: 22px; }

  .holder {
    position: absolute;
    right: 40px; top: 30px;
    width: 250px;
    text-align: right;
  }
  .holder__name {
    color: var(--brand-red);
    font-size: 21px;
    font-weight: 500;
    text-transform: uppercase;
    letter-spacing: .5px;
    white-space: nowrap;
  }
  .holder__role {
    color: var(--soft-white);
    font-size: 14px;
    margin-top: 2px;
    padding-bottom: 6px;
    border-bottom: 1px solid var(--brand-red);
  }
  .edge-tab {
    position: absolute;
    right: 0; top: 30px;
    width: 8px; height: 34px;
    background: var(--brand-red);
  }
  .divider {
    position: absolute;
    left: 34px; right: 40px; top: 150px;
    height: 1px;
    background: var(--brand-red);
  }
  .contacts {
    position: absolute;
    left: 34px; top: 168px;
    list-style: none;
    color: var(--white);
    font-size: 15px;
    line-height: 25px;
  }
  .contacts li { display: flex; align-items: center; gap: 10px; }
  .contacts svg { width: 12px; height: 12px; flex: none; }
  .swoosh { position: absolute; left: 0; bottom: 0; width: 560px; height: 320px; }
</style>
</head>
<body>

<section class="card card--back" aria-label="Card back">
  <div class="brand">
    <span class="brand__name">QV TECHWORKS</span>
    <span class="brand__dot"></span>
  </div>
  <p class="services">
    Managed IT Services<span class="sep">|</span>Productivity Solutions<br>
    Data Backup and Recovery<span class="sep">|</span>IT System Maintenance<span class="sep">|</span>Managed IT Security
  </p>
</section>

<section class="card card--front" aria-label="Card front">
  <svg class="swoosh" viewBox="0 0 560 320" aria-hidden="true">
    <path d="M0 306 L330 306 C350 306 360 270 400 262 L560 262 L560 320 L0 320 Z" fill="#e8202a"/>
    <path d="M0 298 L318 298 L324 292 L0 292 Z" fill="#ffffff"/>
  </svg>
  <div class="edge-tab"></div>
  <div class="brand">
    <span class="brand__name">QV TECHWORKS</span>
    <span class="brand__dot"></span>
  </div>
  <div class="holder">
    <p class="holder__name">Simon Trelawny</p>
    <p class="holder__role">Director</p>
  </div>
  <div class="divider"></div>
  <ul class="contacts">
    <li>
      <svg viewBox="0 0 12 12"><path d="M2 1 L4 1 L5 4 L3.5 5 C4.3 6.7 5.3 7.7 7 8.5 L8 7 L11 8 L11 10 C11 10.6 10.6 11 10 11 C5 11 1 7 1 2 C1 1.4 1.4 1 2 1 Z" fill="#e8202a"/></svg>
      03 6158 4932
    </li>
    <li>
      <svg viewBox="0 0 12 12"><rect x="3" y="0.5" width="6" height="11" rx="1" fill="none" stroke="#e8202a" stroke-width="1.2"/><circle cx="6" cy="9.5" r=".8" fill="#e8202a"/></svg>
      0417 582 139
    </li>
    <li>
      <svg viewBox="0 0 12 12"><rect x="0.8" y="2.5" width="10.4" height="7" fill="none" stroke="#e8202a" stroke-width="1.2"/><path d="M1 3 L6 7 L11 3" fill="none" stroke="#e8202a" stroke-width="1.2"/></svg>
      simon@qvtechworks.com.au
    </li>
    <li>
      <svg viewBox="0 0 12 12"><circle cx="6" cy="6" r="5" fill="none" stroke="#e8202a" stroke-width="1.2"/><path d="M1 6 H11 M6 1 C3.5 3.5 3.5 8.5 6 11 M6 1 C8.5 3.5 8.5 8.5 6 11" fill="none" stroke="#e8202a" stroke-width="1"/></svg>
      www.qvtechworks.com.au
    </li>
  </ul>
</section>

</body>
</html>
```